Website Design for Hulls for Heroes

Please design and code a new website.
Here are the sites I like best:
http://www.wavelorn.com/alternate/
http://www.wheelsforpatriots.org
Please make it similar. This is NOT a car donation site. It's a boat donation site. I just like this sites above as a lead generation sites.
Old site:
http://hullsforheroes.org
Updates
Coding
Coded - Design and coding required
Number of Pages Required
1 page
Look and feel

```html
<!DOCTYPE html>
<html lang="en">
<head>
<meta charset="utf-8">
<title>Hulls for Heroes – Donate Your Boat</title>
<link rel="stylesheet" href="https://fonts.googleapis.com/css2?family=Lato:wght@400;700;900&family=Open+Sans:wght@400;600;700;800&display=swap">
<style>
:root{
  --navy:#1b3a8c;
  --red:#a3231c;
  --red-deep:#7e1a15;
  --gold:#c9a85a;
  --ink:#1d2a5c;
  --text:#333;
  --line:#d5d5d5;
}
*{box-sizing:border-box;margin:0;padding:0}
html,body{width:1200px;height:2679px;overflow:hidden;background:#fff}
body{font-family:"Open Sans",Arial,sans-serif;color:var(--text);position:relative}
.abs{position:absolute}
/* header */
.site-header{left:0;top:0;width:1200px;height:157px;background:linear-gradient(90deg,#1a2447 0%,#2a3566 40%,#5a2630 75%,#3b1f2a 100%)}
.brand{left:36px;top:52px;display:flex;align-items:center;gap:14px}
.brand-mark{width:34px;height:34px;background:var(--gold)}
.brand-name{font-family:"Lato",sans-serif;font-weight:900;font-size:32px;color:var(--gold);letter-spacing:1px;text-transform:uppercase}
.call-box{left:786px;top:0;width:379px;height:157px;background:var(--red);display:flex;align-items:center;padding-left:26px;gap:18px;color:#fff}
.call-box svg{flex:none}
.call-lines .lead{font-family:"Lato",sans-serif;font-weight:900;font-size:22px;line-height:1.1}
.call-lines .num{font-family:"Lato",sans-serif;font-weight:900;font-size:33px;line-height:1.1}
.call-lines .note{font-weight:700;font-size:12.5px}
.nav-bar{left:0;top:157px;width:1200px;height:48px;background:linear-gradient(90deg,#8e2520,#a3231c)}
.main-nav{left:178px;top:157px;height:48px;display:flex;align-items:center;gap:52px}
.main-nav a{color:#fff;text-decoration:none;font-weight:700;font-size:16px}
.online-tab{left:780px;top:157px;width:385px;height:48px;background:#fff;display:flex;align-items:center;justify-content:center;color:var(--red);font-family:"Lato",sans-serif;font-weight:900;font-size:19px}
.tab-icon{left:958px;top:136px;width:30px;height:30px;border-radius:50%;background:var(--red-deep)}
/* hero */
.hero-photo{left:0;top:205px;width:1200px;height:395px;background:linear-gradient(100deg,#4a5040 0%,#7d836e 18%,#c9d4d8 35%,#e6ecef 55%,#bfc8cc 100%)}
.donate-form{left:795px;top:205px;width:357px;height:393px;background:var(--navy);padding:20px 17px}
.donate-form h3{color:#fff;text-align:center;font-size:15.5px;font-weight:700;margin-bottom:11px}
.form-row{display:flex;gap:9px;margin-bottom:8px}
.field{flex:1;height:30px;background:#fff;font-size:12px;font-weight:600;color:var(--ink);padding:6px 6px;position:relative}
.field.select::after{content:"";position:absolute;right:0;top:0;width:26px;height:30px;background:#e6e6e6}
.field.select::before{content:"";position:absolute;right:8px;top:12px;border:5px solid transparent;border-top:6px solid #555;z-index:1}
.submit{display:inline-block;margin-top:8px;background:var(--red);color:#fff;font-weight:700;font-size:15px;padding:9px 25px;border-radius:3px}
.feature-band{left:0;top:598px;width:1200px;height:197px;background:linear-gradient(#ebebeb,#d9d9d9)}
.banner{left:0;top:580px;width:536px;height:238px;background:var(--navy);clip-path:polygon(0 0,90% 0,100% 100%,0 100%);padding:48px 0 0 60px;color:#fff;font-family:"Lato",sans-serif;font-weight:900}
.banner .l1{font-size:27px}
.banner .l2{font-size:58px;color:var(--gold);letter-spacing:2px;line-height:1.1}
.banner .l3{font-size:30px}
.features{left:560px;top:645px;width:560px;display:flex;justify-content:space-between}
.feature{width:130px;text-align:center;font-size:13px;font-weight:700;color:#222;line-height:1.3}
.feature svg{display:block;margin:0 auto 10px}
/* section headings */
.section-title{left:0;width:1200px;display:flex;align-items:center;justify-content:center;gap:26px;font-family:"Lato",sans-serif;font-weight:900;font-size:30px;color:var(--navy)}
.section-title .red{color:var(--red)}
.section-title::before,.section-title::after{content:"";width:130px;height:1px;background:var(--line)}
.section-title.plain::before,.section-title.plain::after{display:none}
/* steps */
.steps{left:78px;top:946px;width:1070px;display:flex;justify-content:space-between}
.step{width:330px;display:flex;gap:14px}
.step svg{flex:none}
.step h4{color:var(--navy);font-size:14px;font-weight:800;margin:22px 0 12px;line-height:1.3}
.step p{font-size:13.5px;font-weight:600;color:#333;line-height:1.45}
/* why */
.why{left:0;top:1157px;width:1200px;height:415px;background:linear-gradient(90deg,#e9ebe8 0%,#f3f3f1 30%,#f0efe9 60%,#d9ddd2 100%)}
.why-list{left:140px;top:1292px;list-style:none}
.why-list li{display:flex;align-items:center;gap:14px;height:33px;font-size:13.5px;color:#333}
.why-list b{color:#222}
.why-list .dot{width:20px;height:20px;border-radius:50%;background:var(--red);position:relative;flex:none}
.why-list .dot::after{content:"";position:absolute;left:6px;top:6px;border-top:4px solid transparent;border-bottom:4px solid transparent;border-left:7px solid #fff}
/* faq */
.faq-photo{left:80px;top:1706px;width:522px;height:416px;background:linear-gradient(160deg,#6f8fbf 0%,#b9474a 40%,#e8e3df 60%,#6a7a3f 100%)}
.faq{left:632px;top:1706px;width:490px}
.faq-item{border:1px solid var(--line);border-radius:8px;padding:0 16px;height:39px;display:flex;align-items:center;justify-content:space-between;font-weight:700;font-size:15px;color:var(--ink);margin-bottom:7px}
.faq-item.open{height:138px;display:block;padding-top:10px}
.faq-item.open .q{display:flex;justify-content:space-between}
.faq-item.open p{font-weight:400;font-size:13px;color:#444;line-height:1.5;margin-top:4px}
.chev{width:9px;height:9px;border-right:2px solid #444;border-bottom:2px solid #444;transform:rotate(45deg);margin-top:-5px}
.chev.up{transform:rotate(-135deg);margin-top:5px}
/* footer */
.footer{left:0;top:2233px;width:1200px;height:407px;background:linear-gradient(120deg,#1d3c95 0%,#234aa8 50%,#1a3785 100%)}
.footer-tab{left:366px;top:2183px;width:474px;height:60px;background:#1f409c;border-radius:40px 40px 0 0;display:flex;align-items:center;justify-content:center;gap:12px}
.footer-tab .brand-mark{width:26px;height:26px}
.footer-tab .brand-name{font-size:26px}
.f-col{top:2357px;color:#fff}
.f-col h5{font-size:14px;font-weight:800;padding-bottom:12px;border-bottom:1px solid rgba(255,255,255,.35);margin-bottom:16px}
.f-col p{font-size:12px;font-weight:700;line-height:1.45}
.f-col a{display:block;color:#fff;text-decoration:none;font-size:13px;font-weight:600;line-height:1.4}
.badge{background:#e7e7e7;border-radius:4px}
.footer-call{left:780px;top:2357px;width:351px;height:149px;border:2px solid #fff;border-radius:8px;display:flex;align-items:center;gap:16px;padding-left:24px;color:#fff}
.copyright{left:0;top:2640px;width:1200px;height:39px;display:flex;align-items:center;justify-content:center;font-size:11.5px;font-weight:700;color:#222}
</style>
</head>
<body>

<header>
  <div class="abs site-header" role="img" aria-label="Waving flag backdrop in dark blue and red"></div>
  <div class="abs brand"><span class="brand-mark"></span><span class="brand-name">Hulls for Heroes</span></div>
  <div class="abs call-box">
    <svg width="62" height="62" viewBox="0 0 62 62"><circle cx="31" cy="31" r="28" fill="none" stroke="#fff" stroke-width="3"/><path d="M21 17c3-2 5 4 6 7 1 2-3 3-2 5 2 4 5 7 9 9 2 1 3-3 5-2 3 1 9 3 7 6-3 6-8 6-14 2-7-4-12-10-14-17-1-4 1-8 3-10z" fill="#fff"/></svg>
    <div class="call-lines"><div class="lead">CALL TODAY TO DONATE</div><div class="num">1-800-555-0142</div><div class="note">Live Operators Available - 7 Days A Week</div></div>
  </div>
  <div class="abs nav-bar"></div>
  <nav class="abs main-nav"><a href="#how">HOW TO DONATE</a><a href="#why">WHY DONATE</a><a href="#faq">FAQ</a><a href="#about">ABOUT</a></nav>
  <div class="abs online-tab">DONATE YOUR BOATS ONLINE</div>
  <div class="abs tab-icon"></div>
</header>

<section>
  <div class="abs hero-photo" role="img" aria-label="Uniformed soldier saluting beside a white motor yacht in front of a city skyline"></div>
  <form class="abs donate-form">
    <h3>Full Tax Deduction - Running or Not</h3>
    <div class="form-row"><div class="field">First Name</div><div class="field">Last Name</div></div>
    <div class="form-row"><div class="field">Daytime Phone</div><div class="field">Email</div></div>
    <div class="form-row"><div class="field">Pickup Address</div></div>
    <div class="form-row"><div class="field">Pickup City</div></div>
    <div class="form-row"><div class="field select">Pickup State</div><div class="field">Zip Code</div></div>
    <div class="form-row"><div class="field select">Choose Year</div><div class="field select">Choose Make</div></div>
    <div class="form-row"><div class="field">Vehicle Model</div></div>
    <div class="submit">DONATE NOW</div>
  </form>
  <div class="abs feature-band"></div>
  <div class="abs banner"><div class="l1">DONATE YOUR BOATS TO</div><div class="l2">VETERANS</div><div class="l3">MAKE A DIFFERENCE</div></div>
  <div class="abs features">
    <div class="feature"><svg width="56" height="56" viewBox="0 0 56 56"><circle cx="28" cy="28" r="25" fill="none" stroke="#a3231c" stroke-width="3"/><path d="M16 28l9 9 17-19" fill="none" stroke="#a3231c" stroke-width="4"/></svg>You have<br>no costs</div>
    <div class="feature"><svg width="60" height="56" viewBox="0 0 60 56"><path d="M6 32h48l-7 10H12z" fill="#a3231c"/><path d="M18 32v-9h20l6 9" fill="#a3231c"/><path d="M4 47c6 3 10-3 17 0s10 3 17 0 11-3 18 0" stroke="#a3231c" stroke-width="2" fill="none"/></svg>Free pickup,<br>running or not</div>
    <div class="feature"><svg width="50" height="56" viewBox="0 0 50 56"><rect x="8" y="3" width="34" height="48" fill="none" stroke="#a3231c" stroke-width="3"/><text x="25" y="33" text-anchor="middle" font-size="18" font-weight="700" fill="#a3231c">$</text><path d="M14 12h22M14 42h22" stroke="#a3231c" stroke-width="2"/></svg>We issue you an<br>IRS tax receipt</div>
    <div class="feature"><svg width="56" height="56" viewBox="0 0 56 56"><rect x="18" y="6" width="30" height="40" fill="none" stroke="#1b3a8c" stroke-width="3"/><circle cx="18" cy="34" r="10" fill="#fff" stroke="#1b3a8c" stroke-width="3"/><path d="M11 41l-7 8" stroke="#1b3a8c" stroke-width="4"/><path d="M28 16h14M30 24h12" stroke="#1b3a8c" stroke-width="2"/></svg>We take care of<br>all paperwork.</div>
  </div>
</section>

<section id="how">
  <h2 class="abs section-title" style="top:870px"><span>HOW TO <span class="red">DONATE</span></span></h2>
  <div class="abs steps">
    <div class="step"><svg width="58" height="78" viewBox="0 0 58 78"><rect x="2" y="0" width="54" height="9" fill="#1b3a8c"/><rect x="12" y="20" width="44" height="9" fill="#1b3a8c"/><rect x="2" y="20" width="7" height="9" fill="#1b3a8c"/><rect x="12" y="40" width="44" height="9" fill="#1b3a8c"/><path d="M4 52l8 18 3-7 8 8 4-4-8-8 7-3z" fill="#1b3a8c"/></svg><div><h4>CALL US AT 1-800-555-0142 OR<br>FILL OUT THE ONLINE FORM</h4><p>Donating your boat is easy and<br>donation is accepted nationwide.</p></div></div>
    <div class="step"><svg width="76" height="50" viewBox="0 0 76 50"><path d="M4 24h68l-10 16H14z" fill="#a3231c"/><path d="M22 24V12h26l8 12" fill="#a3231c"/><rect x="28" y="15" width="6" height="6" fill="#fff"/><rect x="38" y="15" width="6" height="6" fill="#fff"/></svg><div><h4>WE PICK UP THE BOAT</h4><p>Any boats is accepted and we will arrange to pick up your boat when it is most convenient for you.</p></div></div>
    <div class="step"><svg width="70" height="70" viewBox="0 0 70 70"><rect x="14" y="2" width="44" height="58" fill="#fff" stroke="#1b3a8c" stroke-width="2.5"/><rect x="6" y="10" width="44" height="58" fill="#fff" stroke="#1b3a8c" stroke-width="2.5"/><text x="28" y="36" text-anchor="middle" font-size="20" font-weight="700" fill="#1b3a8c">$</text><rect x="16" y="44" width="24" height="14" fill="none" stroke="#1b3a8c" stroke-width="2"/></svg><div><h4>TAX WRITE-OFF</h4><p>Once the boat donation is complete, you will receive your tax deductable boat donation receipt.</p></div></div>
  </div>
</section>

<section id="why">
  <div class="abs why" role="img" aria-label="Faded photo of a kneeling soldier at a memorial with flags"></div>
  <h2 class="abs section-title plain" style="top:1212px"><span>WHY DONATE <span class="red">YOUR BOATS TO US</span></span></h2>
  <ul class="abs why-list">
    <li><span class="dot"></span><span><b>Top Charity Rated &amp; IRS 501(c)3 Approved :</b> Free 24/7 Pickup with No DMV Hassles.</span></li>
    <li><span class="dot"></span><span><b>Free Local Towing :</b> We will pick up your boat donation, running or not, when it's most convenient.</span></li>
    <li><span class="dot"></span><span><b>All Boats Accepted :</b> We take your car regardless of its condition or registration status.</span></li>
    <li><span class="dot"></span><span><b>Income Tax Deduction :</b> We issue you an IRS tax receipt &amp; offer the largest resale network to get you the highest tax write-off possible.</span></li>
    <li><span class="dot"></span><span><b>No Paperwork Hassles :</b> We take any boat and handle everything: DMV, Smog and IRS paperwork.</span></li>
    <li><span class="dot"></span><span><b>Boat donations help fund programs :</b> And benefit National Harbor Veterans Fund. An IRS 501(c)3 nonprofit organization.</span></li>
    <li><span class="dot"></span><span><b>Schedule a Free Pickup :</b> Complete the form and a representative will call you to arrange a convenient time to pickup your boat.</span></li>
  </ul>
</section>

<section id="faq">
  <h2 class="abs section-title" style="top:1627px"><span>FREQUENTLY ASKED <span class="red">QUESTIONS</span></span></h2>
  <div class="abs faq-photo" role="img" aria-label="Rows of small American flags planted in a grassy field"></div>
  <div class="abs faq">
    <div class="faq-item">What types of boats can be donated?<span class="chev"></span></div>
    <div class="faq-item open"><div class="q">What paperwork do I need to donate my boat?<span class="chev up"></span></div><p>All you need is a title, free of all liens. We will request some general information from you at the time of donation such as, the year, make, and model of the boat, as well as its general mechanical condition. We accept all boats, running or non-running.</p></div>
    <div class="faq-item">Is my donated boat tax -deductible?<span class="chev"></span></div>
    <div class="faq-item">What if the boat is not registered in my name?<span class="chev"></span></div>
    <div class="faq-item">How much will I receive as a tax deduction for my boat?<span class="chev"></span></div>
    <div class="faq-item">When will I receive my tax receipt?<span class="chev"></span></div>
    <div class="faq-item">How do I schedule a pick up?<span class="chev"></span></div>
  </div>
</section>

<footer id="about">
  <div class="abs footer"></div>
  <div class="abs footer-tab"><span class="brand-mark"></span><span class="brand-name">Hulls for Heroes</span></div>
  <div class="abs f-col" style="left:72px;width:235px"><h5>ABOUT HULLS FOR HEROES</h5><p>Lorem ipsum dolor sit amet, consectetuer adipiscing elit, sed diam nonummy nibheu ismod tincidunt ut laoreet dolore magna aliquam erat volutpat. Ut wisi enim ad mini veniam, quis nostrud exerci tation ullamcor per suscipit lobortis nisl ut aliquip ex ea co modo consequat.</p></div>
  <div class="abs f-col" style="left:381px;width:110px"><h5>NAVIGATION</h5><a href="#how">HOW TO DONATE</a><a href="#why">WHY DONATE</a><a href="#faq">FAQ</a><a href="#about">ABOUT</a></div>
  <div class="abs f-col" style="left:556px;width:160px"><h5>SAFE &amp; SECURE</h5>
    <div class="badge" style="width:154px;height:52px;margin-bottom:12px"></div>
    <div class="badge" style="width:110px;height:40px;margin-bottom:12px"></div>
    <div class="badge" style="width:56px;height:56px;border-radius:50%"></div>
  </div>
  <div class="abs footer-call">
    <svg width="58" height="58" viewBox="0 0 62 62"><circle cx="31" cy="31" r="28" fill="none" stroke="#fff" stroke-width="3"/><path d="M21 17c3-2 5 4 6 7 1 2-3 3-2 5 2 4 5 7 9 9 2 1 3-3 5-2 3 1 9 3 7 6-3 6-8 6-14 2-7-4-12-10-14-17-1-4 1-8 3-10z" fill="#fff"/></svg>
    <div class="call-lines"><div class="lead" style="font-size:20px">CALL TODAY TO DONATE</div><div class="num" style="font-size:30px">1-800-555-0142</div><div class="note" style="font-size:12px">Live Operators Available - 7 Days A Week</div></div>
  </div>
  <div class="abs copyright">COPYRIGHT © 2017 HULLS FOR HEROES. PRIVACY POLICY I TERMS &amp; CONDITIONS. ALL RIGHTS RESERVED.</div>
</footer>

</body>
</html>
```